Driving-coach/trainer who wants to inform about the offer and how I can help people to drive more re

I need a flyer that informs potential customers about my offer.

DL size 210 mm x 99 mm, vertical!

I'm a trainer/coach who helps people to drive a car more relaxed, without fear and more confident.

It's a one to one training. I do train people in their own car. It gets people their freedom back to go where and when they like to go by own car...

Target Market(s)

People (man an woman) who are afraid of driving a car, or are very stressed while driving....

Industry/Entity Type

Life Coaching

Font styles to use
Sans Serif

Colors
acd136

Requirements
Must have
• Page 1:
• -my offer (see text-pdf)
• -three fotos (see attached files "Pixmarra") of people who are satisfied with my offer
• Page 2:
• -advantages in the work with me.
• -contact information
• -and a picture of me (see attached file) next to the contact information or the advantages of my work
• -my logo (see attached file) on Page 1 + 2
• -i like a "clear" and structured layout. "Less is more"

```html
<!DOCTYPE html>
<html lang="de">
<head>
<meta charset="utf-8">
<title>Flyer – Angstfrei fahren</title>
<link rel="stylesheet" href="https://fonts.googleapis.com/css2?family=Questrial&family=Mulish:wght@700;800;900&display=swap">
<style>
  :root{
    --green:#acd136;
    --green-mid:#a3c94a;
    --green-dark:#8fbf3a;
    --white:#ffffff;
    --ink:#1e1e1e;
    --text:#333333;
    --grey-light:#f4f4f4;
    --grey-mid:#dcdcdc;
    --stage:#9b9b9b;
  }
  *{box-sizing:border-box;margin:0;padding:0}
  html,body{width:1200px;height:1200px;overflow:hidden}
  body{background:var(--stage);position:relative;font-family:"Questrial",sans-serif;color:var(--text)}
  .panel{position:absolute;top:100px;width:478px;height:1014px;overflow:hidden;background:var(--grey-light)}
  .panel--front{left:76px}
  .panel--back{left:647px}
  .panel__bg{position:absolute;inset:0}
  .abs{position:absolute}
  .center{left:0;right:0;text-align:center}
  .header-title{top:0;height:60px;line-height:60px;color:var(--white)}
  .header-title--front{font-size:38px}
  .header-title--back{font-family:"Mulish",sans-serif;font-weight:800;font-size:23px}
  .questions{top:80px;font-size:20px;line-height:30px;color:var(--ink)}
  .headline{font-family:"Mulish",sans-serif;font-weight:900;color:var(--ink);font-size:22px}
  .subline{color:var(--white);font-size:20px;line-height:26px}
  .situations{left:28px;right:22px;top:388px;list-style:none}
  .situations li{position:relative;padding-left:16px;font-size:12.4px;line-height:15.5px;color:#f2f7e4;margin-bottom:11px}
  .situations li b{font-family:"Mulish",sans-serif;font-weight:800;color:var(--white)}
  .situations li svg{position:absolute;left:0;top:3px}
  .steps{top:744px;left:0;width:478px;height:90px}
  .step-label{position:absolute;top:58px;width:160px;text-align:center;font-size:13.5px;line-height:18px;color:var(--ink)}
  .photo{position:absolute}
  .url-bar{position:absolute;left:71px;width:336px;top:984px;height:30px;background:var(--green);color:var(--white);text-align:center;line-height:30px;font-size:15px}
  .advantages{left:26px;right:24px;top:66px;list-style:none}
  .advantages li{position:relative;padding-left:30px;font-size:13.2px;line-height:17.5px;color:var(--text);margin-bottom:9px}
  .advantages li svg{position:absolute;left:0;top:1px}
  .contact{color:var(--white);font-size:17px}
  .contact-title{font-family:"Mulish",sans-serif;font-weight:900;font-size:22px}
  .contact-strong{font-family:"Mulish",sans-serif;font-weight:800;font-size:16px;letter-spacing:.5px}
  .coach-name{left:31px;top:866px;color:var(--green-dark);font-size:19px;letter-spacing:1.5px}
  .coach-role{left:31px;top:892px;color:var(--green-dark);font-size:14px;letter-spacing:1.2px}
</style>
</head>
<body>

<!-- Front page -->
<section class="panel panel--front">
  <svg class="panel__bg" width="478" height="1014" viewBox="0 0 478 1014">
    <defs>
      <linearGradient id="greyFade" x1="0" y1="0" x2="0" y2="1">
        <stop offset="0" stop-color="#fafafa"/><stop offset="1" stop-color="#d9d9d9"/>
      </linearGradient>
      <linearGradient id="greyFade2" x1="0" y1="0" x2="0" y2="1">
        <stop offset="0" stop-color="#f7f7f7"/><stop offset="1" stop-color="#dedede"/>
      </linearGradient>
      <linearGradient id="greenField" x1="0" y1="0" x2="1" y2="1">
        <stop offset="0" stop-color="#b4d55a"/><stop offset=".55" stop-color="#a6cb4c"/><stop offset="1" stop-color="#9cc244"/>
      </linearGradient>
      <radialGradient id="softScene" cx=".55" cy=".45" r=".55">
        <stop offset="0" stop-color="#d6e6a6" stop-opacity=".55"/><stop offset="1" stop-color="#a6cb4c" stop-opacity="0"/>
      </radialGradient>
    </defs>
    <rect width="478" height="1014" fill="url(#greyFade)"/>
    <rect width="478" height="60" fill="var(--green)"/>
    <path d="M0,300 C150,228 330,214 478,236 L478,610 C330,574 150,582 0,650 Z" fill="url(#greenField)"/>
    <rect x="0" y="240" width="478" height="400" fill="url(#softScene)" role="img" aria-label="Faded photo of a smiling woman at the wheel of a car"/>
    <path d="M0,300 C150,228 330,214 478,236" fill="none" stroke="var(--white)" stroke-width="6"/>
    <path d="M0,650 C150,582 330,574 478,610 L478,860 L0,860 Z" fill="url(#greyFade2)"/>
    <path d="M0,650 C150,582 330,574 478,610" fill="none" stroke="var(--white)" stroke-width="6"/>
  </svg>

  <h1 class="abs center header-title header-title--front">Wollen Sie</h1>
  <p class="abs center questions">Fahrangst überwinden?<br>Panikattacken beim<br>Autofahren loswerden?<br>Oder einfach sicher Autofahren?</p>

  <h2 class="abs center headline" style="top:364px;top:264px">Dann sind Sie hier richtig!</h2>
  <p class="abs center subline" style="top:310px">Kommt Ihnen eine dieser Situationen<br>bekannt vor?</p>

  <ul class="abs situations">
    <li><svg width="11" height="10" viewBox="0 0 11 10"><path d="M1,5 L4,8 L10,1" fill="none" stroke="#fff" stroke-width="2"/></svg><b>Angst oder Panikattacken</b> begleiten Sie <b>beim Autofahren.</b> Vielleicht <b>vermeiden</b> Sie deshalb das Autofahren komplett. - Sie möchten angstfrei und/oder ohne Panikattacken fahren.</li>
    <li><svg width="11" height="10" viewBox="0 0 11 10"><path d="M1,5 L4,8 L10,1" fill="none" stroke="#fff" stroke-width="2"/></svg>Sie <b>trauen sich das Autofahren nicht (mehr) zu.</b> - Sie wünschen sich, sicher, entspannt und stressfrei Auto zu fahren.</li>
    <li><svg width="11" height="10" viewBox="0 0 11 10"><path d="M1,5 L4,8 L10,1" fill="none" stroke="#fff" stroke-width="2"/></svg><b>Autofahren</b> erleben Sie unter <b>hoher Anspannung und Stress.</b> - Sie wünschen sich, Autofahren sicher und entspannt zu erleben.</li>
    <li><svg width="11" height="10" viewBox="0 0 11 10"><path d="M1,5 L4,8 L10,1" fill="none" stroke="#fff" stroke-width="2"/></svg>Bestimmte Situationen (z.B. <b>Autobahn, Baustellen, Stadtverkehr</b>...) bereiten Ihnen <b>großen Stress.</b> - Sie möchten diese Situationen souveräner meistern.</li>
  </ul>

  <h2 class="abs center headline" style="top:664px">Das muss nicht so bleiben!</h2>
  <p class="abs center" style="top:700px;font-size:19px;color:var(--ink)">3 Schritte zur Lösung:</p>

  <div class="abs steps">
    <svg width="478" height="40" viewBox="0 0 478 40" style="position:absolute;top:0;left:0">
      <line x1="64" y1="18" x2="382" y2="18" stroke="var(--green-dark)" stroke-width="1.5" stroke-dasharray="2 3"/>
      <circle cx="64" cy="18" r="16" fill="var(--green-mid)"/>
      <circle cx="214" cy="18" r="16" fill="var(--green-mid)"/>
      <circle cx="382" cy="18" r="16" fill="var(--green-mid)"/>
      <text x="64" y="25" text-anchor="middle" font-family="Mulish, sans-serif" font-weight="900" font-size="19" fill="#fff">1</text>
      <text x="214" y="25" text-anchor="middle" font-family="Mulish, sans-serif" font-weight="900" font-size="19" fill="#fff">2</text>
      <text x="382" y="25" text-anchor="middle" font-family="Mulish, sans-serif" font-weight="900" font-size="19" fill="#fff">3</text>
    </svg>
    <p class="step-label" style="left:-16px">Erstgespräch<br>vereinbaren</p>
    <p class="step-label" style="left:134px;width:172px;left:128px">Analyse Ihrer individuellen<br>Situation und Zielsetzung</p>
    <p class="step-label" style="left:302px">Individuelles<br>Coaching und Training</p>
  </div>

  <svg class="photo" style="left:0;top:854px" width="239" height="160" role="img" aria-label="Photo of a smiling woman driving a convertible">
    <defs><linearGradient id="photoConvertible" x1="0" y1="0" x2="1" y2="1"><stop offset="0" stop-color="#6b5a4c"/><stop offset=".5" stop-color="#a58a6e"/><stop offset="1" stop-color="#4a4a4a"/></linearGradient></defs>
    <rect width="239" height="160" fill="url(#photoConvertible)"/>
  </svg>
  <svg class="photo" style="left:244px;top:854px" width="234" height="160" role="img" aria-label="Photo of a young woman giving a thumbs up from a car window">
    <defs><linearGradient id="photoThumbs" x1="0" y1="0" x2="1" y2="1"><stop offset="0" stop-color="#bcc79a"/><stop offset=".5" stop-color="#e2d2b4"/><stop offset="1" stop-color="#c9ccd0"/></linearGradient></defs>
    <rect width="234" height="160" fill="url(#photoThumbs)"/>
  </svg>

  <p class="url-bar">www.angstfrei-fahren-coach.de</p>
</section>

<!-- Back page -->
<section class="panel panel--back">
  <svg class="panel__bg" width="478" height="1014" viewBox="0 0 478 1014">
    <defs>
      <linearGradient id="greyList" x1="0" y1="0" x2="0" y2="1">
        <stop offset="0" stop-color="#f9f9f9"/><stop offset="1" stop-color="#e3e3e3"/>
      </linearGradient>
      <linearGradient id="greyFoot" x1="0" y1="0" x2="0" y2="1">
        <stop offset="0" stop-color="#f5f5f5"/><stop offset="1" stop-color="#d8d8d8"/>
      </linearGradient>
    </defs>
    <rect width="478" height="1014" fill="url(#greyList)"/>
    <rect width="478" height="60" fill="var(--green)"/>
    <rect y="494" width="478" height="320" fill="var(--green-mid)"/>
    <path d="M0,800 C140,740 330,730 478,746 L478,1014 L0,1014 Z" fill="url(#greyFoot)"/>
    <path d="M0,800 C140,740 330,730 478,746" fill="none" stroke="var(--white)" stroke-width="6"/>
  </svg>

  <h1 class="abs center header-title header-title--back">Advantages in the work with me</h1>

  <ul class="abs advantages">
    <li><svg width="16" height="16" viewBox="0 0 16 16"><circle cx="8" cy="8" r="8" fill="var(--green-mid)"/><path d="M4,8 L7,11 L12,5" fill="none" stroke="#fff" stroke-width="2"/></svg>über 10 Jahre Erfahrung als Trainerin und Coach im Bereich Fahrsicherheit.</li>
    <li><svg width="16" height="16" viewBox="0 0 16 16"><circle cx="8" cy="8" r="8" fill="var(--green-mid)"/><path d="M4,8 L7,11 L12,5" fill="none" stroke="#fff" stroke-width="2"/></svg>Als psychotherapeutische Heilpraktikerin bin ich auf Angststörungen und Panikattacken spezialisiert</li>
    <li><svg width="16" height="16" viewBox="0 0 16 16"><circle cx="8" cy="8" r="8" fill="var(--green-mid)"/><path d="M4,8 L7,11 L12,5" fill="none" stroke="#fff" stroke-width="2"/></svg>100 % auf Sie zugeschnitten: ich hole Sie genau dort ab, wo Sie jetzt stehen und unterstütze Sie in Ihrem Prozess individuell und zielführend.</li>
    <li><svg width="16" height="16" viewBox="0 0 16 16"><circle cx="8" cy="8" r="8" fill="var(--green-mid)"/><path d="M4,8 L7,11 L12,5" fill="none" stroke="#fff" stroke-width="2"/></svg>Wenn es Ihnen nicht möglich ist, in meine Praxis nach Neustadt Süd zu kommen: Mit der mobilen Praxis komme ich auch zu Ihnen.</li>
    <li><svg width="16" height="16" viewBox="0 0 16 16"><circle cx="8" cy="8" r="8" fill="var(--green-mid)"/><path d="M4,8 L7,11 L12,5" fill="none" stroke="#fff" stroke-width="2"/></svg>Termine sind auch abends und am Wochenende möglich.</li>
  </ul>

  <svg class="photo" style="left:0;top:335px" width="239" height="159" role="img" aria-label="Photo of a small yellow car with luggage on the roof in a summer field">
    <defs><linearGradient id="photoYellowCar" x1="0" y1="0" x2="0" y2="1"><stop offset="0" stop-color="#3f7fc4"/><stop offset=".42" stop-color="#8fb4d8"/><stop offset=".55" stop-color="#5d7a3a"/><stop offset=".75" stop-color="#d9c23a"/><stop offset="1" stop-color="#a99a5c"/></linearGradient></defs>
    <rect width="239" height="159" fill="url(#photoYellowCar)"/>
  </svg>
  <svg class="photo" style="left:244px;top:335px" width="234" height="159" role="img" aria-label="Photo of a young woman giving a thumbs up from a car window">
    <defs><linearGradient id="photoThumbsBack" x1="0" y1="0" x2="1" y2="1"><stop offset="0" stop-color="#bcc79a"/><stop offset=".5" stop-color="#e2d2b4"/><stop offset="1" stop-color="#c9ccd0"/></linearGradient></defs>
    <rect width="234" height="159" fill="url(#photoThumbsBack)"/>
  </svg>

  <p class="abs center contact contact-title" style="top:526px">CONTACT:</p>
  <p class="abs center contact" style="top:562px;font-size:19px">Katrin Lehmbach</p>
  <p class="abs center contact" style="top:593px">Weitere Informationen finden Sie auf:</p>
  <svg class="abs" style="left:232px;top:622px" width="14" height="14" viewBox="0 0 14 14">
    <circle cx="7" cy="7" r="6" fill="none" stroke="#fff" stroke-width="1.3"/>
    <ellipse cx="7" cy="7" rx="2.6" ry="6" fill="none" stroke="#fff" stroke-width="1.1"/>
    <line x1="1" y1="7" x2="13" y2="7" stroke="#fff" stroke-width="1.1"/>
  </svg>
  <p class="abs center contact" style="top:640px;font-size:16px">www.angstfrei-fahren-coach.de</p>
  <p class="abs center contact" style="top:666px">Oder rufen Sie mich einfach an:</p>
  <svg class="abs" style="left:231px;top:696px" width="16" height="16" viewBox="0 0 16 16">
    <circle cx="8" cy="8" r="7" fill="none" stroke="#fff" stroke-width="1.3"/>
    <path d="M5.4,4.6 L6.8,4.4 L7.4,6.2 L6.6,7 Q7.4,8.8 9,9.4 L9.8,8.6 L11.6,9.2 L11.4,10.6 Q8,11.4 5.4,4.6 Z" fill="#fff"/>
  </svg>
  <p class="abs center contact contact-strong" style="top:718px">0151 23 45 67 89</p>

  <svg class="photo" style="left:277px;top:728px" width="201" height="286" role="img" aria-label="Portrait photo of the coach in a white blouse">
    <defs><radialGradient id="photoPortrait" cx=".45" cy=".45" r=".6"><stop offset="0" stop-color="#e9ddd2"/><stop offset=".6" stop-color="#f3f3f3"/><stop offset="1" stop-color="#e0e0e0" stop-opacity="0"/></radialGradient></defs>
    <rect width="201" height="286" fill="url(#photoPortrait)"/>
  </svg>

  <p class="abs coach-name">Katrin Lehmbach</p>
  <p class="abs coach-role">Fahrangst–Bewältigungs–Coach</p>

  <p class="url-bar">www.angstfrei-fahren-coach.de</p>
</section>

</body>
</html>
```